TIDAL VERGE needs bisness cards pronto

Bisness name is "TIDAL VERGE" new bisness the bisness includes lawn mowing, garden matanace, and any jobs around the house.
I need a card that is colorful and vibrant and the bisness of lawn mowing maybe with some nature with it. It also needs my contact details"Darren Quellby mobile 0413562049 call for free quote and email norma.vance@fernmail.com.au and a catchy tag line

Industry/Entity Type

House

Requirements
Must have
• Bisness name "TIDAL VERGE"
Contact details "0413562049"
Email norma.vance@fernmail.com.au
Call for free quote

```html
<!DOCTYPE html>
<html lang="en">
<head>
<meta charset="utf-8">
<title>Tidal Verge – Business Card</title>
<link href="https://fonts.googleapis.com/css2?family=Open+Sans:ital,wght@0,400;0,700;0,800;1,400&display=swap" rel="stylesheet">
<style>
  :root {
    --backdrop: #d6eee0;
    --card: #ffffff;
    --ink: #1c1c1c;
    --brand-green: #6cc04a;
    --leaf-deep: #1f8f4e;
    --leaf-mid: #3fae6c;
    --leaf-soft: #9fd9b5;
    --leaf-mist: #e3f4ea;
  }

  * { margin: 0; padding: 0; box-sizing: border-box; }

  html, body {
    width: 1200px;
    height: 646px;
    overflow: hidden;
  }

  body {
    background: var(--backdrop);
    font-family: "Open Sans", Arial, sans-serif;
    color: var(--ink);
  }

  .card {
    position: absolute;
    left: 120px;
    top: 30px;
    width: 960px;
    height: 586px;
    background: var(--card);
    overflow: hidden;
    box-shadow: 0 10px 30px rgba(30, 90, 60, 0.18);
  }

  .floral-art {
    position: absolute;
    left: 0;
    top: 90px;
    width: 620px;
    height: 496px;
    background:
      radial-gradient(ellipse 28% 34% at 42% 52%, var(--leaf-deep) 0%, var(--leaf-mid) 45%, transparent 75%),
      radial-gradient(ellipse 48% 50% at 45% 50%, var(--leaf-soft) 0%, var(--leaf-mist) 60%, transparent 85%);
  }

  .brand {
    position: absolute;
    left: 560px;
    top: 38px;
    display: flex;
    align-items: center;
    gap: 14px;
  }

  .brand-name {
    font-weight: 800;
    font-size: 62px;
    line-height: 0.92;
    letter-spacing: 1px;
    color: var(--brand-green);
  }

  .contact {
    position: absolute;
    right: 42px;
    top: 240px;
    text-align: right;
  }

  .tagline {
    font-style: italic;
    font-size: 27px;
    margin-bottom: 34px;
  }

  .person {
    font-weight: 700;
    font-size: 40px;
    line-height: 1.1;
  }

  .mobile {
    font-size: 27px;
    margin-bottom: 34px;
  }

  .email {
    font-weight: 700;
    font-size: 29px;
    white-space: nowrap;
  }
</style>
</head>
<body>
  <main class="card">
    <div class="floral-art" role="img" aria-label="Translucent green flower illustration with swirls and bubbles"></div>

    <div class="brand">
      <div class="brand-name">TIDAL<br>VERGE</div>
    </div>

    <section class="contact">
      <p class="tagline">Call for a free quote</p>
      <p class="person">Darren Quellby</p>
      <p class="mobile">mob 0413 562 049</p>
      <p class="email">Email: norma.vance@fernmail.com.au</p>
    </section>
  </main>
</body>
</html>
```